Daniel Fordyce Psychotherapy Business Card Design Project

I need a welcoming business card for a Somatic Psychotherapy private practice based in Melbourne, Australia. I help individual clients to work through issues in their life that are inhibiting achieving their full potential. I would like a san serif font and the oculars are:
blue: R:37 G:61 B:95 C:93 M:77 Y:38 K:28
orange: R:241 G:103 B:43 C:0 M:74 Y:93 K:0
The final design should communicate warm, welcoming and safe environment in which clients are supported to grow. It should also convey a collaborative approach to achieve success between me (the therapist) and the client. The uploaded file is my new logo. Also an organic look and feel while maintaining professionalism and a clean, simple look is sought after.
In addition to the logo my details are:
Daniel Fordyce
Psychotherapist
B.Arts., Grad Dip. T&D., Dip.Som.Psych, MRTOB, MFLENG
0417 552 908
dfordyce@danielfordyce.com.au
www.danielfordyce.com.au
Psychotherapy Clients
Environment

```html
<!DOCTYPE html>
<html lang="en">
<head>
<meta charset="utf-8">
<title>Daniel Fordyce Psychotherapy – Business Card</title>
<link rel="stylesheet" href="https://fonts.googleapis.com/css2?family=Source+Sans+3:wght@400;600;700&display=swap">
<style>
  :root {
    --navy: #253d5f;
    --orange: #f1672b;
    --ink: #3c3c3c;
    --card: #ffffff;
    --backdrop: #e9e6e2;
  }
  * { box-sizing: border-box; margin: 0; padding: 0; }
  html, body {
    width: 1200px; height: 415px; overflow: hidden;
    background: var(--backdrop);
    font-family: "Source Sans 3", Arial, sans-serif;
  }
  .stage { position: relative; width: 1200px; height: 415px; }
  .card {
    position: absolute; top: 60px; width: 525px; height: 300px;
    background: var(--card); border-radius: 20px; overflow: hidden;
    box-shadow: 0 2px 6px rgba(0,0,0,.18);
  }
  .card--front { left: 55px; }
  .card--back { left: 632px; }

  .brand {
    position: absolute; left: 0; right: 0;
    text-align: center;
    color: var(--navy); font-weight: 600; font-size: 36px; line-height: 1.02;
  }
  .brand span { display: block; }
  .card--front .brand { top: 56px; }
  .card--back .brand { top: 113px; }

  .details { position: absolute; top: 158px; left: 0; right: 0; text-align: center; color: var(--ink); }
  .details__name { font-size: 17px; color: var(--navy); font-weight: 700; line-height: 20px; }
  .details__name .role { font-size: 13px; font-weight: 400; color: var(--ink); }
  .details__creds { margin-top: 7px; font-size: 13px; line-height: 16px; }
  .contact { margin-top: 18px; display: flex; justify-content: center; gap: 10px; font-size: 13px; align-items: center; }
  .contact__item { display: inline-flex; align-items: center; gap: 5px; }
  .contact__item svg { display: block; }

  .band { position: absolute; left: 0; bottom: 0; width: 525px; height: 46px; }
  .band__url {
    position: absolute; right: 32px; bottom: 14px; color: #fff;
    font-size: 14px; letter-spacing: 1.6px; line-height: 16px;
  }
  .back-url {
    position: absolute; left: 0; right: 0; bottom: 23px; text-align: center;
    font-size: 14px; letter-spacing: 2px; color: var(--ink); line-height: 16px;
  }
</style>
</head>
<body>
<main class="stage">
  <section class="card card--front" aria-label="Card front">
    <div class="brand"><span>Daniel Fordyce</span><span>Psychotherapy</span></div>
    <div class="details">
      <p class="details__name">Daniel Fordyce , <span class="role">Psychotherapist</span></p>
      <p class="details__creds">B.Arts., Grad Dip. T&amp;D., Dip.Som.Psych, MRTOB, MFLENG</p>
      <p class="contact">
        <span class="contact__item">
          <svg width="11" height="11" viewBox="0 0 24 24" aria-hidden="true"><path fill="#444" d="M6.6 10.8a15 15 0 0 0 6.6 6.6l2.2-2.2a1 1 0 0 1 1-.25 11.4 11.4 0 0 0 3.6.57 1 1 0 0 1 1 1V20a1 1 0 0 1-1 1A17 17 0 0 1 3 4a1 1 0 0 1 1-1h3.5a1 1 0 0 1 1 1c0 1.25.2 2.45.57 3.57a1 1 0 0 1-.25 1z"/></svg>
          0417 552 908
        </span>
        <span class="contact__item">
          <svg width="10" height="8" viewBox="0 0 10 8" aria-hidden="true"><rect width="10" height="8" fill="#444"/><path d="M0 0l5 4 5-4" fill="none" stroke="#fff" stroke-width="1"/></svg>
          dfordyce@danielfordyce.com.au
        </span>
      </p>
    </div>
    <svg class="band" viewBox="0 0 525 46" aria-hidden="true">
      <polygon points="0,0 253,0 241,13 0,13" fill="var(--orange)"/>
      <polygon points="0,18 238,18 255,0 525,0 525,46 0,46" fill="var(--navy)"/>
    </svg>
    <span class="band__url">www.danielfordyce.com.au</span>
  </section>

  <section class="card card--back" aria-label="Card back">
    <div class="brand"><span>Daniel Fordyce</span><span>Psychotherapy</span></div>
    <p class="back-url">www.danielfordyce.com.au</p>
  </section>
</main>
</body>
</html>
```